Healthcare Recruitment Agency Brochure

We need our current Brochure updated as its old and dated. The brochure will be for our current and potential Clients and should provide all the necessary information regarding our services, but in a well presented, easy reading format which echoes our company Brand. The company supplies Healthcare establishments with trained healthcare Staff which can be in a variety of settings.
UPDATE: Following the submission of many designs we would like to amend the information/content to be included in the brochure and have uploaded additional information. We would like an 8 page booklet with the various sections spread out so as not to look to 'wordy' page 1 Front cover, 2 About Us, 3 Our Service, 4 Our promise, 5 Our Staff, 6 Our Ethos, 7 What Our Clients Say/Testimonials, 8 Contact Us/Back page. Please if using pictures (which is welcomed) steer away from the surgical/doctor type. We mainly provide care to the Elderly within Nursing and Residential Homes and Support Environments. Thanks
Updates

Target Market(s)

Healthcare clientell

Industry/Entity Type

Healthcare

Requirements
Must have
• Pictures, animation, easy reading, informative, tie in with website theme www.carewellstaffline.example
Nice to have
• open to ideas
Should not have
• very long text paragraphs

```html
<!DOCTYPE html>
<html lang="en">
<head>
<meta charset="utf-8">
<title>Carewell Staffline – Brochure Spreads</title>
<link href="https://fonts.googleapis.com/css2?family=Montserrat:ital,wght@0,400;0,500;0,600;0,700;1,500;1,600&family=Open+Sans:ital,wght@0,400;0,600;0,700;1,400&display=swap" rel="stylesheet">
<style>
  :root{
    --bg:#4f4f4f;
    --paper:#f4f4f4;
    --paper-shade:#ebebeb;
    --teal:#17a589;
    --navy:#1f3f93;
    --ink:#2b2b2b;
    --muted:#555;
    --photo-green:#5f8a3a;
    --photo-warm:#c98a64;
    --photo-sky:#c7d3dc;
  }
  *{box-sizing:border-box;margin:0;padding:0}
  html,body{width:858px;height:1200px;overflow:hidden}
  body{background:var(--bg);font-family:"Open Sans",Arial,sans-serif;color:var(--ink);position:relative}
  .spread{position:absolute;left:29px;width:800px;height:566px;display:flex;box-shadow:0 10px 30px rgba(0,0,0,.35)}
  .spread--outer{top:28px}
  .spread--inner{top:606px}
  .page{position:relative;width:400px;height:566px;background:var(--paper);overflow:hidden}
  .page + .page{border-left:1px solid #dcdcdc}
  .page-title{font-family:"Montserrat",sans-serif;font-weight:600;color:var(--teal);font-size:15px;letter-spacing:.5px;text-transform:uppercase}
  .edge-band{position:absolute;bottom:0;height:4px}
  .footer{position:absolute;left:26px;bottom:14px;display:flex;align-items:center;gap:6px;font-size:5.2px;color:#333}
  .footer-badge{width:10px;height:7px;background:var(--navy)}
  .brand{display:flex;align-items:center;gap:7px;font-family:"Montserrat",sans-serif;font-weight:500;color:var(--teal);font-size:17px}
  .brand-dot{width:12px;height:12px;border-radius:50%;background:var(--navy)}
  .photo{position:absolute}
  .checklist{list-style:none}
  .checklist li{position:relative;padding-left:14px;margin-bottom:5px}
  .checklist li svg{position:absolute;left:0;top:1px}
  strong{font-weight:700}

  /* Ethos page */
  .ethos{padding:40px 40px 0 34px}
  .ethos .page-title{margin-bottom:12px}
  .ethos-company{font-family:"Montserrat",sans-serif;font-style:italic;font-weight:600;color:var(--navy);font-size:8.5px;margin-bottom:18px}
  .value{margin-bottom:18px;font-size:7.6px;line-height:1.4;color:#333}
  .value-name{font-family:"Montserrat",sans-serif;font-style:italic;font-weight:500;color:var(--teal);font-size:8.5px}
  .value-initial{font-size:22px;font-style:normal;line-height:.8;margin-right:1px}
  .value p{text-align:justify;margin-top:2px}
  .ethos .brand{position:absolute;left:34px;top:372px}

  /* Cover */
  .cover .photo{left:40px;top:48px;width:300px;height:345px;background:linear-gradient(135deg,var(--photo-green),#88a85a 45%,var(--photo-warm) 75%,#e06a4a)}
  .cover .brand{position:absolute;left:58px;top:430px;font-size:22px}
  .cover .brand-dot{width:15px;height:15px}

  /* About */
  .about{padding:28px 26px 0 26px}
  .about .page-title{margin-bottom:8px}
  .about-intro{width:215px;font-size:7.1px;line-height:1.38}
  .about-intro p{margin-bottom:5px;text-align:justify}
  .about .photo--team{right:22px;top:118px;width:120px;height:120px;background:radial-gradient(circle at 50% 45%,#dfe9f1,#fff 75%)}
  .about-banner{position:absolute;left:0;right:0;top:246px;height:48px;background:var(--teal);color:#fff;font-family:"Montserrat",sans-serif;font-size:9.6px;line-height:1.35;padding:9px 26px}
  .about-list{position:absolute;left:26px;top:306px;width:200px;font-size:7px;line-height:1.35}
  .about .photo--care{right:22px;top:312px;width:130px;height:160px;background:linear-gradient(160deg,#8fb06b,#6d8f5a 50%,#5a7ea8)}
  .about .edge-band{left:0;width:100%;background:var(--navy)}

  /* Staff */
  .staff{padding:40px 0 0 24px}
  .staff .page-title{margin-bottom:8px}
  .staff-lead{width:205px;font-size:7.4px;line-height:1.38;margin-bottom:8px}
  .staff-list{width:205px;font-size:7.2px;line-height:1.35}
  .staff-list li{margin-bottom:6px}
  .staff .photo{right:0;top:22px;width:150px;height:215px;background:linear-gradient(150deg,#e7d7c6,#c9a48a 45%,#eef0f2 80%)}
  .staff-note{position:absolute;right:18px;top:250px;width:140px;font-size:7.2px;line-height:1.38;text-align:justify}
  .staff-note p{margin-bottom:7px}
</style>
</head>
<body>
<svg width="0" height="0" style="position:absolute" aria-hidden="true">
  <symbol id="tick-box" viewBox="0 0 10 10">
    <rect x="0.7" y="0.7" width="8.6" height="8.6" fill="none" stroke="#333" stroke-width="1"/>
    <path d="M2.3 5.2 4.2 7 7.8 2.8" fill="none" stroke="#333" stroke-width="1.2"/>
  </symbol>
</svg>

<!-- Outer spread: back page and front cover -->
<section class="spread spread--outer">
  <article class="page ethos">
    <h2 class="page-title">Our Ethos</h2>
    <p class="ethos-company">Carewell Staffline Services Ltd</p>

    <div class="value">
      <span class="value-name"><span class="value-initial">H</span>onesty and Integrity.</span>
      <p>We pride ourselves on being direct and straightforward in all our communication with our clients and potential candidates.</p>
    </div>
    <div class="value">
      <span class="value-name"><span class="value-initial">D</span>edication.</span>
      <p>Our consultants aim to fully understand the requirements of our clients and candidates in order to find mutually beneficial solutions</p>
    </div>
    <div class="value">
      <span class="value-name"><span class="value-initial">S</span>ervice Excellence.</span>
      <p>We aim to always deliver superior services to help both employers and candidates achieve their goals.</p>
    </div>
    <div class="value">
      <span class="value-name"><span class="value-initial">L</span>eadership.</span>
      <p>Our purpose is to become leaders in the healthcare recruitment sector, raising the bar for the entire industry.</p>
    </div>

    <div class="brand"><span class="brand-dot"></span>Carewell Staffline</div>

    <footer class="footer"><span class="footer-badge"></span>Registered in England No. 12045873 Carewell Staffline Services Ltd, 14 Orchard Row, Ashford, Kent, TN23 1XY</footer>
    <div class="edge-band" style="left:0;width:60%;background:var(--navy)"></div>
    <div class="edge-band" style="left:60%;width:40%;background:var(--teal)"></div>
  </article>

  <article class="page cover">
    <div class="photo" role="img" aria-label="Smiling carer standing behind an elderly woman in a wheelchair in a leafy garden"></div>
    <div class="brand"><span class="brand-dot"></span>Carewell Staffline</div>
    <div class="edge-band" style="left:0;width:62%;background:var(--teal)"></div>
  </article>
</section>

<!-- Inner spread: About Us and Our Staff -->
<section class="spread spread--inner">
  <article class="page about">
    <h2 class="page-title">About Us</h2>
    <div class="about-intro">
      <p>With over <strong>15 years</strong> of experience <strong>Carewell Staffline</strong> specialises in reliable recruitment solutions for the healthcare sector.</p>
      <p>We are <strong>RSA accredited</strong> so you can rest assured that we will always be working in line with current legislation and guidelines.</p>
      <p>We strive for excellence in every aspect of our service, this includes ensuring that we are always fair, honest and supportive of our temporary staff members, which is why we are a National Living Wage Employer.</p>
    </div>
    <div class="photo photo--team" role="img" aria-label="Group of care workers in light uniforms joining hands"></div>

    <div class="about-banner">We know that our Clients often have a lot on their plate, which is why we pride ourselves on being extremely accommodating:</div>

    <ul class="checklist about-list">
      <li><svg width="8" height="8"><use href="#tick-box"/></svg>We can visit you at a time to suit you, to discuss your requirements and our service.</li>
      <li><svg width="8" height="8"><use href="#tick-box"/></svg>We will give you our client application pack including everything you need to know, to start booking staff from Carewell Staffline we simply need a completed client account form.</li>
      <li><svg width="8" height="8"><use href="#tick-box"/></svg>We have staff available to work at the drop of a hat-we understand the need for urgency and will make it our mission to try to help you every time.</li>
      <li><svg width="8" height="8"><use href="#tick-box"/></svg>Our friendly office staff will always be at the end of the phone to deal with your requests, we never outsource to call centres.</li>
      <li><svg width="8" height="8"><use href="#tick-box"/></svg>We will never leave you waiting and always be honest and realistic in telling you whether we can help.</li>
      <li><svg width="8" height="8"><use href="#tick-box"/></svg>When you have booked a staff member you will always receive their compliance form, in a format that suits you.</li>
    </ul>
    <div class="photo photo--care" role="img" aria-label="Carer kneeling beside an elderly man in a wheelchair outdoors"></div>

    <footer class="footer"><span class="footer-badge"></span>Registered in England No. 12045873 Carewell Staffline Services Ltd, 14 Orchard Row, Ashford, Kent, TN23 1XY</footer>
    <div class="edge-band"></div>
  </article>

  <article class="page staff">
    <h2 class="page-title">Our Staff</h2>
    <p class="staff-lead">All our candidates go through a thorough vetting and recruitment process and only ever commence assignments after the following:</p>
    <ul class="checklist staff-list">
      <li><svg width="8" height="8"><use href="#tick-box"/></svg>A face-to-face interview and skills assessment has been undertaken</li>
      <li><svg width="8" height="8"><use href="#tick-box"/></svg>Full employment history has been submitted</li>
      <li><svg width="8" height="8"><use href="#tick-box"/></svg>Right to work has been recorded and verified</li>
      <li><svg width="8" height="8"><use href="#tick-box"/></svg>Fitness to work has been declared</li>
      <li><svg width="8" height="8"><use href="#tick-box"/></svg>Two work related references have been obtained and verified</li>
      <li><svg width="8" height="8"><use href="#tick-box"/></svg>An enhanced DBS Certificate has been provided</li>
      <li><svg width="8" height="8"><use href="#tick-box"/></svg>In date, sufficient training certificates have been provided and verified or in house training courses have been attended and certificates have been issued.</li>
      <li><svg width="8" height="8"><use href="#tick-box"/></svg>Registration with the appropriate bodies has been verified for Registered Nurses.</li>
      <li><svg width="8" height="8"><use href="#tick-box"/></svg>A shadow shift has been completed if it is a brand new staff member</li>
      <li><svg width="8" height="8"><use href="#tick-box"/></svg>An ID Badge, uniform, and timesheets have been issued</li>
    </ul>

    <div class="photo" role="img" aria-label="Smiling carer holding hands with a laughing elderly woman"></div>
    <div class="staff-note">
      <p>We understand that it is imperative for our clients to only have extremely competent, fully trained staff supporting their existing team. We are proud to cover the standards set within the <strong>Care Certificate</strong> in the training modules that we deliver to our staff.</p>
      <p>All training is refreshed on an annual basis and we ensure that up to date certificates are held by all staff at all times</p>
    </div>

    <footer class="footer"><span class="footer-badge"></span>Registered in England No. 12045873 Carewell Staffline Services Ltd, 14 Orchard Row, Ashford, Kent, TN23 1XY</footer>
  </article>
</section>
</body>
</html>
```